Mobile Friendly Lead Generation Landing Page

We are a web marketing company that specialized in web lead generation. Recently we have started buying media from mobile devices and we need a mobile interface(landing page) where we can collect user data in an effective manner.

Our current mobile landing page is:
http://www.tuitionscout.example.com/lp13d/index.aspx?a=true&source=581406
Through this you can see what the steps/questions users need to answer to get matched to a school. We need the design for the whole process.

We are pretty open for design ideas and our goal is to make this mobile optimized landing page have the look and feel of an app...but not an app.
There are several questions in the process but we are open to changing the way they are presented. As in, you can have one question at a time or a few.
The goal is to make this EXTREMELY EASY for users to interact with.

One example that we have liked is:
http://lessonhub.example/schools/47215-page1.lhub (please note that this opens only on mobile devices)

Some of these screenshots are attached.

Our web form looks like this:
http://www.tuitionscout.example.com/lp88/index.aspx?a=true

```html
<!DOCTYPE html>
<html lang="en">
<head>
<meta charset="utf-8">
<title>TuitionScoutApp – Mobile Match Flow</title>
<link rel="stylesheet" href="https://fonts.googleapis.com/css2?family=Roboto:wght@400;500;700&family=Roboto+Condensed:wght@700&display=swap">
<style>
  :root {
    --canvas: #f3f4f5;
    --screen: #ffffff;
    --brand: #1b93c4;
    --brand-light: #2aa5da;
    --brand-dark: #157eb0;
    --accent: #ff8200;
    --field-border: #86c6de;
    --muted: #9a9a9a;
    --ink: #1d1d1d;
    --chrome: #f7f7f7;
    --url-bar: #e4e5e7;
    --picker: #ececed;
    --picker-line: #cfcfd1;
  }
  * { box-sizing: border-box; margin: 0; padding: 0; }
  html, body {
    width: 1200px; height: 1000px; overflow: hidden;
    background: var(--canvas);
    font-family: "Roboto", Arial, sans-serif;
  }
  .screen {
    position: absolute; top: 178px;
    width: 360px; height: 634px;
    background: var(--screen);
    overflow: hidden;
    box-shadow: 0 0 0 4px #2a2a2a;
  }
  .screen--form { left: 178px; }
  .screen--picker { left: 670px; }

  /* status bar */
  .status-bar {
    position: absolute; top: 0; left: 0; right: 0; height: 22px;
    font-size: 12px; color: #111;
  }
  .status-bar__signal { position: absolute; left: 8px; top: 4px; display: flex; align-items: center; gap: 6px; }
  .status-bar__time { position: absolute; left: 0; right: 0; top: 4px; text-align: center; font-weight: 500; }
  .status-bar__battery { position: absolute; right: 8px; top: 4px; display: flex; align-items: center; gap: 4px; }

  .url-bar {
    position: absolute; top: 26px; left: 12px; width: 334px; height: 32px;
    background: var(--url-bar); border-radius: 5px;
    font-size: 17px; color: #222; text-align: center; line-height: 32px;
  }
  .url-bar svg { position: absolute; right: 9px; top: 7px; }

  /* app header */
  .app-header {
    position: absolute; top: 70px; left: 0; right: 0; height: 72px;
    background: var(--brand); color: #fff;
  }
  .brand {
    position: absolute; left: 12px; top: 0; height: 72px;
    display: flex; align-items: center; gap: 10px;
    font-family: "Roboto Condensed", Arial, sans-serif; font-weight: 700; font-size: 25px;
  }
  .brand__dot { width: 22px; height: 22px; border-radius: 50%; background: #fff; }
  .progress {
    position: absolute; right: 0; top: 0; width: 104px; height: 72px;
    border-left: 1px solid rgba(255,255,255,.55);
    text-align: center; padding-top: 20px; font-size: 14px; line-height: 18px;
  }
  .progress strong { display: block; font-size: 15px; }

  /* ribbon */
  .ribbon { position: absolute; top: 163px; left: 16px; width: 328px; height: 56px; }
  .ribbon__text {
    position: absolute; left: 28px; top: 0; width: 272px; height: 40px;
    display: flex; align-items: center; justify-content: center; gap: 8px;
    color: #fff; font-size: 17px;
  }

  /* questions */
  .question {
    position: absolute; left: 16px; width: 240px;
    font-size: 16px; line-height: 22px; color: var(--muted);
  }
  .question__step { color: var(--brand); font-weight: 700; margin-right: 4px; }
  .select-field {
    position: absolute; left: 15px; width: 326px; height: 50px;
    border: 1px solid var(--field-border); border-radius: 5px;
    font-size: 18px; color: var(--brand); padding-left: 13px; line-height: 48px;
  }
  .select-field svg { position: absolute; right: 12px; top: 14px; }

  .button {
    position: absolute; left: 15px; width: 326px; height: 50px; border-radius: 5px;
    color: #fff; font-size: 18px; text-align: center; line-height: 50px;
  }
  .button--next { top: 502px; background: var(--brand); font-weight: 700; }
  .button--back { top: 561px; background: var(--accent); }

  /* picker */
  .picker-toolbar {
    position: absolute; top: 338px; left: 0; right: 0; height: 50px;
    background: var(--chrome); border-top: 1px solid #d8d8d8;
    font-size: 15px; color: #111; text-align: right; padding-right: 9px; line-height: 48px;
  }
  .picker-wheel {
    position: absolute; top: 388px; left: 0; right: 0; bottom: 0;
    background: linear-gradient(#f2f2f3, var(--picker) 40%, #e4e4e6);
    font-family: "Roboto", Arial, sans-serif;
  }
  .picker-option { position: absolute; left: 50px; font-size: 20px; color: #8a8a8a; white-space: nowrap; }
  .picker-option--placeholder { left: 24px; top: 44px; font-size: 17px; color: #b4b8c0; display: flex; gap: 10px; align-items: center; }
  .picker-option--faint { top: 73px; }
  .picker-option--current { top: 107px; left: 48px; font-size: 22px; color: var(--ink); }
  .picker-option--below { top: 144px; }
  .picker-option--lower { top: 174px; font-size: 17px; color: #7b7b7b; }
  .picker-option--edge { top: 199px; font-size: 13px; color: #9a9a9a; letter-spacing: .5px; }
  .picker-line { position: absolute; left: 0; right: 0; height: 1px; background: var(--picker-line); }
  .touch-glow {
    position: absolute; left: 30px; top: 110px; width: 290px; height: 130px;
    background: radial-gradient(ellipse at center, rgba(60,205,255,.85) 0%, rgba(80,210,255,.45) 40%, rgba(120,220,255,0) 70%);
    pointer-events: none;
  }
</style>
</head>
<body>

<!-- Screen: question form -->
<section class="screen screen--form">
  <div class="status-bar">
    <div class="status-bar__signal">
      <svg width="38" height="8" viewBox="0 0 38 8"><circle cx="4" cy="4" r="3.3" fill="#111"/><circle cx="11.5" cy="4" r="3.3" fill="#111"/><circle cx="19" cy="4" r="3.3" fill="#111"/><circle cx="26.5" cy="4" r="3" fill="none" stroke="#111"/><circle cx="34" cy="4" r="3" fill="none" stroke="#111"/></svg>
      <span>NX</span>
      <svg width="14" height="11" viewBox="0 0 14 11"><path d="M7 10 L1 3.5 A9 9 0 0 1 13 3.5 Z" fill="#111"/></svg>
    </div>
    <div class="status-bar__time">19:44</div>
    <div class="status-bar__battery">50%
      <svg width="26" height="12" viewBox="0 0 26 12"><rect x=".5" y=".5" width="22" height="11" rx="2" fill="none" stroke="#111"/><rect x="2" y="2" width="10" height="8" fill="#111"/><rect x="23.5" y="4" width="2" height="4" fill="#111"/></svg>
    </div>
  </div>
  <div class="url-bar">tuitionscout.example.com
    <svg width="17" height="18" viewBox="0 0 17 18"><path d="M14 10 A6 6 0 1 1 10 4.3" fill="none" stroke="#333" stroke-width="2"/><path d="M8 1 L12 4.5 L8 8" fill="none" stroke="#333" stroke-width="2"/></svg>
  </div>
  <header class="app-header">
    <div class="brand"><span class="brand__dot"></span>TuitionScoutApp</div>
    <div class="progress">PROGRESS<strong>0%</strong></div>
  </header>
  <div class="ribbon">
    <svg width="328" height="56" viewBox="0 0 328 56">
      <polygon points="0,12 44,12 44,56 0,56 14,34" fill="#1a86c0"/>
      <polygon points="328,12 284,12 284,56 328,56 314,34" fill="#1a86c0"/>
      <polygon points="28,40 44,56 44,40" fill="#0f5f8c"/>
      <polygon points="300,40 284,56 284,40" fill="#0f5f8c"/>
      <rect x="28" y="0" width="272" height="40" fill="#2aa5da"/>
    </svg>
    <div class="ribbon__text"><span>Get matched in <strong>2 minutes</strong></span>
      <svg width="22" height="22" viewBox="0 0 22 22"><circle cx="11" cy="11" r="9.5" fill="none" stroke="#fff" stroke-width="2"/><path d="M11 5 V11 H15" fill="none" stroke="#fff" stroke-width="2"/></svg>
    </div>
  </div>
  <p class="question" style="top:242px"><span class="question__step">1/10</span>Please select your field of interest from the following</p>
  <div class="select-field" style="top:295px">Select
    <svg width="14" height="22" viewBox="0 0 14 22"><path d="M2 2 L11 11 L2 20" fill="none" stroke="#1b93c4" stroke-width="2.5"/></svg>
  </div>
  <p class="question" style="top:370px"><span class="question__step">2/10</span>What is Your Current Education Level?</p>
  <div class="select-field" style="top:425px">Select
    <svg width="14" height="22" viewBox="0 0 14 22"><path d="M2 2 L11 11 L2 20" fill="none" stroke="#1b93c4" stroke-width="2.5"/></svg>
  </div>
  <div class="button button--next">Next</div>
  <div class="button button--back">Back</div>
</section>

<!-- Screen: option picker open -->
<section class="screen screen--picker">
  <div class="status-bar">
    <div class="status-bar__signal">
      <svg width="38" height="8" viewBox="0 0 38 8"><circle cx="4" cy="4" r="3.3" fill="#111"/><circle cx="11.5" cy="4" r="3.3" fill="#111"/><circle cx="19" cy="4" r="3.3" fill="#111"/><circle cx="26.5" cy="4" r="3" fill="none" stroke="#111"/><circle cx="34" cy="4" r="3" fill="none" stroke="#111"/></svg>
      <span>NX</span>
      <svg width="14" height="11" viewBox="0 0 14 11"><path d="M7 10 L1 3.5 A9 9 0 0 1 13 3.5 Z" fill="#111"/></svg>
    </div>
    <div class="status-bar__time">19:44</div>
    <div class="status-bar__battery">50%
      <svg width="26" height="12" viewBox="0 0 26 12"><rect x=".5" y=".5" width="22" height="11" rx="2" fill="none" stroke="#111"/><rect x="2" y="2" width="10" height="8" fill="#111"/><rect x="23.5" y="4" width="2" height="4" fill="#111"/></svg>
    </div>
  </div>
  <div class="url-bar">tuitionscout.example.com
    <svg width="17" height="18" viewBox="0 0 17 18"><path d="M14 10 A6 6 0 1 1 10 4.3" fill="none" stroke="#333" stroke-width="2"/><path d="M8 1 L12 4.5 L8 8" fill="none" stroke="#333" stroke-width="2"/></svg>
  </div>
  <header class="app-header">
    <div class="brand"><span class="brand__dot"></span>TuitionScoutApp</div>
    <div class="progress">PROGRESS<strong>0%</strong></div>
  </header>
  <div class="ribbon">
    <svg width="328" height="56" viewBox="0 0 328 56">
      <polygon points="0,12 44,12 44,56 0,56 14,34" fill="#1a86c0"/>
      <polygon points="328,12 284,12 284,56 328,56 314,34" fill="#1a86c0"/>
      <polygon points="28,40 44,56 44,40" fill="#0f5f8c"/>
      <polygon points="300,40 284,56 284,40" fill="#0f5f8c"/>
      <rect x="28" y="0" width="272" height="40" fill="#2aa5da"/>
    </svg>
    <div class="ribbon__text"><span>Get matched in <strong>2 minutes</strong></span>
      <svg width="22" height="22" viewBox="0 0 22 22"><circle cx="11" cy="11" r="9.5" fill="none" stroke="#fff" stroke-width="2"/><path d="M11 5 V11 H15" fill="none" stroke="#fff" stroke-width="2"/></svg>
    </div>
  </div>
  <p class="question" style="top:242px"><span class="question__step">1/10</span>Please select your field of interest from the following</p>
  <div class="select-field" style="top:295px">Select
    <svg width="14" height="22" viewBox="0 0 14 22"><path d="M2 2 L11 11 L2 20" fill="none" stroke="#1b93c4" stroke-width="2.5"/></svg>
  </div>

  <div class="picker-toolbar">Done</div>
  <div class="picker-wheel">
    <div class="picker-option picker-option--placeholder">
      <svg width="18" height="14" viewBox="0 0 18 14"><path d="M1 7 L6 12 L17 1" fill="none" stroke="#b4b8c0" stroke-width="2.5"/></svg>
      - Please Select -
    </div>
    <div class="picker-option picker-option--faint">A mobile project</div>
    <div class="picker-line" style="top:102px"></div>
    <div class="picker-option picker-option--current">A web project</div>
    <div class="picker-line" style="top:141px"></div>
    <div class="picker-option picker-option--below">Both</div>
    <div class="picker-option picker-option--lower">Just a chat!</div>
    <div class="picker-option picker-option--edge">Another, even better reason!</div>
    <div class="touch-glow"></div>
  </div>
</section>

</body>
</html>
```